Web Design Project for lawn care business

after having a logo designed now my website is letting me down.
My websites main purpose is once i have made contact with a customer most will then try to research my company and the work i have done. Going to my unprofessional and untidy site will only put off potential customers. Also some customers will find my site online so must be able to grab their attention.

My site must be in keeping with my logo. Which is modern, sleek and classy. It needs to convey how professional we are and that the customer is getting a professional service.

My existing site will be replaced with the winning design.

Content wise and amount of pages will be similar to mine how ever more data will be inputted by myself.

so far prefer sites designed incorporating links in pictures or animated links to flick through pictures etc

breaks up the site and is more user friendly. 

also need to make sure colours are in keeping with logo or at least have similarities to keep it all uniform.

thanks

Industry/Entity Type

Lawn Care

Requirements
Nice to have
• in keeping font wise with my logo
same colours etc

```html
<!DOCTYPE html>
<html lang="en">
<head>
<meta charset="utf-8">
<title>Fairway Lawn Care – Tree, Garden &amp; Lawn</title>
<link rel="stylesheet" href="https://fonts.googleapis.com/css2?family=Encode+Sans+Condensed:wght@500;600&family=PT+Sans:wght@400;700&display=swap">
<style>
  :root {
    --black: #000000;
    --lime: #8cbb1f;
    --lime-light: #a6d12c;
    --lime-dark: #6e9a14;
    --lime-text: #9ccc2a;
    --page: #f3f3f3;
    --frame: #d9d9d9;
    --text: #3a3a3a;
    --white: #ffffff;
    --footer: #161616;
  }
  * { box-sizing: border-box; margin: 0; padding: 0; }
  html, body { width: 1200px; height: 1200px; overflow: hidden; background: var(--page); }
  body { position: relative; font-family: "PT Sans", sans-serif; color: var(--text); }

  .site-header { position: absolute; left: 0; top: 0; width: 1200px; height: 114px; background: var(--black); }
  .brand { position: absolute; left: 165px; top: 20px; display: flex; align-items: center; gap: 12px; }
  .brand-mark { width: 62px; height: 62px; border-radius: 50%; background: var(--lime); }
  .brand-name { font-family: "Encode Sans Condensed", sans-serif; font-weight: 500; font-size: 28px; line-height: 1; color: var(--lime-text); letter-spacing: .5px; white-space: nowrap; }
  .brand-tag { font-family: "Encode Sans Condensed", sans-serif; font-weight: 500; font-size: 11px; color: var(--lime-text); letter-spacing: .5px; margin-top: 6px; }

  .call-box { position: absolute; left: 803px; top: 14px; width: 237px; height: 37px; border: 1px solid #3a3a3a; display: flex; align-items: center; padding-left: 12px; gap: 7px; white-space: nowrap; }
  .call-box span { font-size: 12px; color: #e6e6e6; font-weight: 700; }
  .call-box strong { font-size: 17px; color: var(--lime-text); font-weight: 400; }

  .search { position: absolute; left: 834px; top: 62px; width: 205px; height: 38px; background: var(--white); border: 3px solid #888; border-radius: 3px; }
  .search svg { position: absolute; left: 10px; top: 9px; }
  .search-btn { position: absolute; right: 3px; top: 3px; width: 61px; height: 26px; background: var(--lime); color: var(--white); font-size: 13px; font-weight: 700; display: flex; align-items: center; justify-content: center; }

  .main-nav { position: absolute; left: 0; top: 114px; width: 1200px; height: 36px; background: linear-gradient(var(--lime-light), var(--lime-dark)); }
  .main-nav a { position: absolute; top: 0; height: 36px; display: flex; align-items: center; justify-content: center; color: var(--white); font-family: "Encode Sans Condensed", sans-serif; font-weight: 500; font-size: 15px; text-decoration: none; border-right: 1px solid rgba(0,0,0,.25); white-space: nowrap; }

  .slider { position: absolute; left: 168px; top: 158px; width: 877px; height: 336px; background: var(--white); border: 1px solid var(--frame); padding: 4px; box-shadow: 0 12px 14px -8px rgba(0,0,0,.35); }
  .slide-photo { width: 100%; height: 100%; background: linear-gradient(#5f7a4c 0%, #7a8f5e 25%, #8a9a5e 45%, #7d8f52 100%); position: relative; }
  .slide-caption { position: absolute; left: 40px; top: 236px; color: var(--white); font-family: "Encode Sans Condensed", sans-serif; font-weight: 500; font-size: 27px; line-height: 31px; text-align: center; white-space: nowrap; }
  .slider-arrow { position: absolute; top: 294px; width: 42px; height: 74px; background: var(--lime); display: flex; align-items: center; justify-content: center; }
  .slider-arrow.prev { left: 127px; border-radius: 37px 0 0 37px; }
  .slider-arrow.next { left: 1045px; border-radius: 0 37px 37px 0; }

  .service { position: absolute; width: 282px; }
  .service-frame { height: 166px; background: var(--white); border: 1px solid var(--frame); padding: 5px; }
  .service-photo { position: relative; height: 100%; }
  .service-title { position: absolute; left: 0; right: 0; bottom: 0; height: 30px; background: rgba(0,0,0,.45); color: var(--white); font-family: "Encode Sans Condensed", sans-serif; font-weight: 500; font-size: 17px; display: flex; align-items: center; padding-left: 10px; white-space: nowrap; }
  .service p { font-size: 12px; line-height: 18px; margin-top: 6px; height: 36px; overflow: hidden; letter-spacing: -.1px; }
  .more { display: inline-block; margin: 8px 0 0 3px; background: var(--lime); color: #2d3b08; font-size: 13px; padding: 3px 8px; }

  .site-footer { position: absolute; left: 0; top: 1051px; width: 1200px; height: 149px; background: radial-gradient(ellipse at 50% 20%, #2e2e2e, var(--footer) 70%); color: var(--white); }
  .footer-head { position: absolute; top: 25px; font-family: "Encode Sans Condensed", sans-serif; font-weight: 600; font-size: 13px; white-space: nowrap; }
  .social { position: absolute; left: 176px; top: 52px; display: flex; gap: 7px; }
  .social span { width: 20px; height: 20px; border-radius: 3px; }
  .newsletter { position: absolute; left: 820px; top: 49px; display: flex; gap: 5px; }
  .newsletter .field { width: 156px; height: 25px; background: var(--white); color: #555; font-size: 11px; padding: 5px 8px; }
  .newsletter .btn { height: 25px; background: var(--lime); color: #1d2a05; font-size: 13px; padding: 4px 5px; }
  .footer-rule { position: absolute; left: 168px; top: 93px; width: 884px; height: 1px; background: #3a3a3a; }
  .footer-links { position: absolute; left: 168px; top: 111px; font-size: 11px; color: #ddd; word-spacing: 2px; white-space: nowrap; }
  .copyright { position: absolute; left: 873px; top: 111px; font-size: 11px; color: #ddd; white-space: nowrap; }
</style>
</head>
<body>
  <header class="site-header">
    <div class="brand">
      <div class="brand-mark"></div>
      <div>
        <div class="brand-name">FAIRWAY LAWN CARE</div>
        <div class="brand-tag">TREE, GARDEN &amp; LAWN</div>
      </div>
    </div>
    <div class="call-box">
      <svg width="14" height="20" viewBox="0 0 14 20"><path d="M3 1 L6 1 L7 6 L5 7 Q6 12 9 14 L11 12 L13 15 L11 19 Q2 16 1 4 Z" fill="#ddd"/></svg>
      <span>CALL US NOW</span><strong>01632 960 418</strong>
    </div>
    <div class="search">
      <svg width="14" height="14" viewBox="0 0 14 14"><circle cx="5" cy="5" r="3.5" fill="none" stroke="#999" stroke-width="2"/><line x1="7.5" y1="7.5" x2="12" y2="12" stroke="#999" stroke-width="2.5"/></svg>
      <div class="search-btn">SEARCH</div>
    </div>
  </header>

  <nav class="main-nav">
    <a style="left:165px;width:119px">HOME</a>
    <a style="left:284px;width:119px">ABOUT US</a>
    <a style="left:403px;width:108px">OUR SERVICES</a>
    <a style="left:511px;width:121px">USEFUL LINKS</a>
    <a style="left:632px;width:154px">LAWNCARE ADVICE</a>
    <a style="left:786px;width:120px">FAQS</a>
    <a style="left:906px;width:132px;border-right:none">CONTACT US</a>
  </nav>

  <section class="slider">
    <div class="slide-photo" role="img" aria-label="Groundsman driving a green compact tractor with a spreader across a fairway lined with palm trees">
      <div class="slide-caption">FAIRWAY LAWN CARE<br>TREE GARDEN &amp; LAWN SERVICES</div>
    </div>
  </section>
  <div class="slider-arrow prev"><svg width="14" height="22" viewBox="0 0 14 22"><path d="M11 2 L3 11 L11 20" fill="none" stroke="#fff" stroke-width="3.5"/></svg></div>
  <div class="slider-arrow next"><svg width="14" height="22" viewBox="0 0 14 22"><path d="M3 2 L11 11 L3 20" fill="none" stroke="#fff" stroke-width="3.5"/></svg></div>

  <article class="service" style="left:170px;top:530px">
    <div class="service-frame"><div class="service-photo" role="img" aria-label="Arborist cutting a branch with a chainsaw" style="background:linear-gradient(#c9d6d4,#6f8a5a 60%,#4a5a38)"><div class="service-title">TREE SERVICES</div></div></div>
    <p>Tree pruning, Tree shapping, Tree felling<br>Tree stump removal</p>
    <span class="more">MORE</span>
  </article>
  <article class="service" style="left:466px;top:530px">
    <div class="service-frame"><div class="service-photo" role="img" aria-label="Red lawn mower on grass in front of a hedge" style="background:linear-gradient(#3f7a2a,#5c9a34 55%,#7fb048)"><div class="service-title">GARDEN SERVICES</div></div></div>
    <p>One off tidy ups, Regular maintenance programmes<br>tailored to your requirements, Hedge cutting...</p>
    <span class="more">MORE</span>
  </article>
  <article class="service" style="left:764px;top:530px">
    <div class="service-frame"><div class="service-photo" role="img" aria-label="Ride-on mower cutting a bright green lawn" style="background:linear-gradient(#6aa03a,#8fc24a 50%,#5a9a2a)"><div class="service-title">LAWN SERVICES</div></div></div>
    <p>Tree pruning, Tree shapping, Tree felling<br>Tree stump removal</p>
    <span class="more">MORE</span>
  </article>

  <article class="service" style="left:170px;top:791px">
    <div class="service-frame"><div class="service-photo" role="img" aria-label="Turf machine working on a stadium pitch" style="background:linear-gradient(#c9a93a,#b89a3a 35%,#3f8a3a 55%,#2f7a2f)"><div class="service-title">SPORTS SURFACE SERVICES</div></div></div>
    <p>Tree pruning, Tree shapping, Tree felling<br>Tree stump removal</p>
    <span class="more">MORE</span>
  </article>
  <article class="service" style="left:466px;top:791px">
    <div class="service-frame"><div class="service-photo" role="img" aria-label="Handshake between two business people" style="background:linear-gradient(120deg,#2a4a4a,#5a7a78 50%,#d8d2c0)"><div class="service-title">OUR COMMITMENT</div></div></div>
    <p>All waste removed, Fully Insured, Fully qualified<br>greenkeepers...</p>
    <span class="more">MORE</span>
  </article>
  <article class="service" style="left:764px;top:791px">
    <div class="service-frame"><div class="service-photo" role="img" aria-label="Two colleagues shaking hands in an office" style="background:linear-gradient(90deg,#e8e8e8,#f6f6f6 50%,#cfcfcf)"><div class="service-title">ABOUT US</div></div></div>
    <p>As the name suggests all work is carried out by fully<br>qualified Greenkeepers so why do it yourself?</p>
    <span class="more">MORE</span>
  </article>

  <footer class="site-footer">
    <div class="footer-head" style="left:175px">FOLLOW US ON</div>
    <div class="social" aria-label="Social links">
      <span style="background:#3b5b98"></span><span style="background:#1a7bb0"></span><span style="background:#2aa4d8"></span><span style="background:#f08a24"></span>
    </div>
    <div class="footer-head" style="left:931px">NEWSLETTER SUBSCRIBE</div>
    <div class="newsletter"><div class="field">Enter the Email id</div><div class="btn">Subscribe</div></div>
    <div class="footer-rule"></div>
    <div class="footer-links">Home &nbsp;| &nbsp;About Us | &nbsp;Our Services &nbsp;| &nbsp;Useful Links &nbsp;| &nbsp;Lawncare Advice &nbsp;| &nbsp;FAQS | &nbsp;Contact Us</div>
    <div class="copyright">Copyrights @ 2013 All Rights Reserved</div>
  </footer>
</body>
</html>
```